Internet of Things integrator needs logo and website design

We need a logo and website design for our company ("Brightwave Link"). We integrate IoT(Internet of Things) projects including: devices, network and sw solutions for all type of vertical markets. The image should be professional like the following site: quorvel.io clear and easy surfing, and should include about the same sections shown in that website (Why Us?, Products, Resources, Company, etc). Website colors should follow logo colors (logo has to be designed and aproved first). The logo should be something like the one used at tandemvexa.com (image attached), where we could use the logo to susbtitute the letter "o" in "IoT". The final design should communicate professionalism and experience.

Coding

Coded - Design and coding required

Number of Pages Required

5+ page

Font styles to use
Other font styles liked:
• see quorvel.io wensite

Requirements
Must have
• Serious and professional look and feel as in: quorvel.io website.
The following pages should be included:
- home page
- Why Us?
- Products
- Resources
- Company
- Newsroom
- Contact
Nice to have
• High tech look and feel
Should not have
• Fun or not serious images (cartoons, etc.)

```html
<!DOCTYPE html>
<html lang="en">
<head>
<meta charset="utf-8">
<title>Brightwave Link – Resources</title>
<link href="https://fonts.googleapis.com/css2?family=Poppins:wght@400;500;600;700;800&display=swap" rel="stylesheet">
<style>
  :root{
    --navy:#14196b;
    --ink:#1d1d2b;
    --muted:#8a8fa3;
    --blue:#1f7ef0;
    --blue-deep:#1a2fc9;
    --blue-light:#2aa7f6;
    --white:#ffffff;
    --tint-purple:#ece6fb;
    --tint-grey:#efefef;
    --tint-blue:#e1ebfc;
    --tint-yellow:#fdf6dc;
  }
  *{box-sizing:border-box;margin:0;padding:0}
  html,body{width:716px;height:1200px;overflow:hidden;background:var(--white)}
  body{font-family:"Poppins",sans-serif;color:var(--ink);position:relative}

  .site-header{position:absolute;top:0;left:0;width:716px;height:54px;display:flex;align-items:center;padding:0 30px 0 52px}
  .brand{font-size:17px;font-weight:700;color:var(--navy);letter-spacing:-.2px;display:flex;align-items:center;gap:6px;white-space:nowrap}
  .brand-dot{width:9px;height:9px;border-radius:50%;background:var(--blue)}
  .main-nav{margin-left:auto;display:flex;align-items:center;gap:18px;font-size:10.5px;font-weight:600}
  .main-nav a{color:var(--ink);text-decoration:none}
  .main-nav a.is-active{color:var(--blue)}
  .btn-contact{background:linear-gradient(90deg,var(--blue-light),var(--blue-deep));color:var(--white)!important;border-radius:16px;padding:8px 14px;font-size:9.5px;font-weight:700;letter-spacing:.3px}

  .page-title{position:absolute;top:108px;width:716px;text-align:center}
  .page-title h1{font-size:26px;font-weight:800;color:var(--navy);letter-spacing:.5px;line-height:1}
  .crumbs{font-size:10px;color:var(--ink);margin-top:6px}

  .resource-grid{position:absolute;top:178px;left:53px;display:grid;grid-template-columns:repeat(3,197px);column-gap:11px;row-gap:31px}
  .resource-card{text-align:center}
  .cover{height:222px;border-radius:6px;display:flex;align-items:center;justify-content:center}
  .cover-art{width:62%;height:70%;border-radius:3px}
  .tint-purple{background:var(--tint-purple)}
  .tint-grey{background:var(--tint-grey)}
  .tint-blue{background:var(--tint-blue)}
  .tint-yellow{background:var(--tint-yellow)}
  .category{font-size:7.5px;color:var(--muted);margin-top:10px;letter-spacing:.4px;text-transform:uppercase}
  .resource-title{font-size:11px;font-weight:700;color:var(--navy);line-height:1.25;margin-top:3px;text-transform:uppercase}
  .read-link{display:inline-block;font-size:8px;font-weight:700;color:var(--blue);margin-top:4px;border-bottom:1px solid var(--blue);padding-bottom:1px}

  .site-footer{position:absolute;top:880px;left:0;width:716px;height:320px;color:var(--white)}
  .footer-wave{position:absolute;top:0;left:0}
  .footer-inner{position:absolute;top:96px;left:0;width:716px}
  .footer-brand{position:absolute;left:52px;top:56px;font-size:17px;font-weight:700;display:flex;align-items:center;gap:6px;white-space:nowrap;letter-spacing:-.2px}
  .footer-brand .brand-dot{background:var(--white);width:9px;height:9px}
  .footer-col{position:absolute;top:8px}
  .footer-col h4{font-size:12px;font-weight:600;margin-bottom:8px}
  .footer-col ul{list-style:none;font-size:8.5px;line-height:1.75}
  .col-links{left:232px}
  .col-news{left:349px}
  .col-contact{left:540px}
  .news-note{font-size:8.5px;margin-bottom:8px}
  .news-input{width:140px;height:22px;border-radius:11px;background:var(--white);color:var(--muted);font-size:8px;padding:5px 12px}
  .news-btn{margin-top:8px;width:86px;height:22px;border:1px solid var(--white);border-radius:11px;font-size:8px;font-weight:600;display:flex;align-items:center;justify-content:center;letter-spacing:.4px}
  .contact-row{display:flex;align-items:center;gap:6px}
  .socials{display:flex;gap:8px;margin-top:6px}
  .socials span{width:8px;height:8px;border-radius:50%;background:var(--white);display:block}
  .copyright{position:absolute;bottom:12px;width:716px;text-align:center;font-size:8px}
  .scroll-top{position:absolute;right:14px;bottom:64px;width:22px;height:22px;border-radius:50%;background:var(--white)}
</style>
</head>
<body>
  <header class="site-header">
    <div class="brand">Brightwave Link <span class="brand-dot"></span></div>
    <nav class="main-nav">
      <a href="#">Why Us?</a>
      <a href="#">Products</a>
      <a href="#" class="is-active">Resources</a>
      <a href="#">Company</a>
      <a href="#">Newsroom</a>
      <a href="#" class="btn-contact">CONTACT US</a>
    </nav>
  </header>

  <section class="page-title">
    <h1>RESOURCES</h1>
    <p class="crumbs">Home / Resources</p>
  </section>

  <main class="resource-grid">
    <article class="resource-card">
      <div class="cover tint-purple"><div class="cover-art" role="img" aria-label="Whitepaper book cover mockup" style="background:linear-gradient(135deg,#8f7be8,#3b4fd6)"></div></div>
      <p class="category">Whitepaper</p>
      <h3 class="resource-title">IoT Industrial Edge<br>Computing Platform</h3>
      <span class="read-link">READ</span>
    </article>
    <article class="resource-card">
      <div class="cover tint-grey"><div class="cover-art" role="img" aria-label="White paper brochure mockup" style="background:linear-gradient(135deg,#2e3a4f,#6ec6c9)"></div></div>
      <p class="category">White Paper</p>
      <h3 class="resource-title">Repurposing Legacy<br>Systems for Industrial IoT</h3>
      <span class="read-link">READ</span>
    </article>
    <article class="resource-card">
      <div class="cover tint-blue"><div class="cover-art" role="img" aria-label="Research report cover mockup" style="background:linear-gradient(160deg,#ffffff,#3a8ef0)"></div></div>
      <p class="category">Report</p>
      <h3 class="resource-title">Harlow &amp; Penn Industrial<br>IoT Platforms Research</h3>
      <span class="read-link">READ</span>
    </article>
    <article class="resource-card">
      <div class="cover tint-blue"><div class="cover-art" role="img" aria-label="Whitepaper book cover mockup" style="background:linear-gradient(160deg,#3b5ee0,#243a9c)"></div></div>
      <p class="category">Whitepaper</p>
      <h3 class="resource-title">IoT Industrial Edge<br>Computing Platform</h3>
      <span class="read-link">READ</span>
    </article>
    <article class="resource-card">
      <div class="cover tint-yellow"><div class="cover-art" role="img" aria-label="White paper book cover mockup" style="background:linear-gradient(160deg,#f4f4f4,#e6b4d8)"></div></div>
      <p class="category">White Paper</p>
      <h3 class="resource-title">Repurposing Legacy<br>Systems for Industrial IoT</h3>
      <span class="read-link">READ</span>
    </article>
    <article class="resource-card">
      <div class="cover tint-blue"><div class="cover-art" role="img" aria-label="Research report book cover mockup" style="background:linear-gradient(160deg,#6a4fd8,#2d3aa8)"></div></div>
      <p class="category">Report</p>
      <h3 class="resource-title">Harlow &amp; Penn Industrial<br>IoT Platforms Research</h3>
      <span class="read-link">READ</span>
    </article>
  </main>

  <footer class="site-footer">
    <svg class="footer-wave" width="716" height="320" viewBox="0 0 716 320" aria-hidden="true">
      <defs>
        <linearGradient id="footerBlue" x1="0" y1="0" x2="1" y2="0.3">
          <stop offset="0" stop-color="#2aa7f6"/>
          <stop offset="1" stop-color="#1a2fc9"/>
        </linearGradient>
      </defs>
      <path d="M0 30 C180 10 420 110 716 0 L716 320 L0 320 Z" fill="url(#footerBlue)"/>
    </svg>
    <div class="footer-inner">
      <div class="footer-brand">Brightwave Link <span class="brand-dot"></span></div>
      <div class="footer-col col-links">
        <h4>Useful Links</h4>
        <ul><li>Why Us?</li><li>Products</li><li>Resources</li><li>Company</li><li>Newsroom</li><li>Contact Us</li></ul>
      </div>
      <div class="footer-col col-news">
        <h4>Newsletter</h4>
        <p class="news-note">Subscribe to our newsletter</p>
        <div class="news-input">Email Address</div>
        <div class="news-btn">SUBSCRIBE</div>
      </div>
      <div class="footer-col col-contact">
        <h4>Contact Us</h4>
        <ul>
          <li class="contact-row"><svg width="8" height="9" viewBox="0 0 8 10"><path d="M4 0a3.5 3.5 0 0 1 3.5 3.5C7.5 6 4 10 4 10S.5 6 .5 3.5A3.5 3.5 0 0 1 4 0z" fill="#fff"/></svg>12 Harbor Lane Suite 4</li>
          <li class="contact-row"><svg width="8" height="8" viewBox="0 0 10 10"><path d="M2 0l2 2.5-1.2 1.3a6 6 0 0 0 3.4 3.4L7.5 6 10 8l-1.5 2C4 10 0 6 0 1.5z" fill="#fff"/></svg>+1 555 0142 386</li>
          <li class="contact-row"><svg width="9" height="7" viewBox="0 0 10 8"><rect width="10" height="8" rx="1" fill="#fff"/><path d="M0 1l5 3.5L10 1" stroke="#1f7ef0" fill="none"/></svg>hello@brightwave.io</li>
        </ul>
        <div class="socials"><span></span><span></span><span></span></div>
      </div>
    </div>
    <div class="scroll-top"></div>
    <p class="copyright">Copyright 2020 | All Rights Reserved</p>
  </footer>
</body>
</html>
```